"Sketch Onward Club" Social Art Website Design

I need a design for a website I am building, which will be called Sketch Onward Club. I have attached the selected logo for the site. The site will be about drawing/art, and how art can be used to brighten a stranger's day as a random act of kindness. In real life, people will receive a drawing or piece of art with details for this site on it. They will in turn be able to give a drawing or piece of art to someone else, thus building a 'chain' of people who are related to each other through the drawings they have received. This should create a strong 'social' aspect to the site. There will be areas of the site for seeing other drawings/art that have been submitted, as well as for seeing different statistics (how many drawings have been submitted, where, how people are connected, etc.).

Target Market(s)

No specific target market.

Industry/Entity Type

Building

Coding

Number of Pages Required

1 page

Font styles to use
Sans Serif
Decorative

Requirements
Must have
• Must use the logo supplied.
Nice to have
• Should be colourful and artistic. References to art tools should be primarily around drawing, though painting can also feature. Colour scheme to match the logo would be ideal.

```html
<!DOCTYPE html>
<html lang="en">
<head>
<meta charset="utf-8">
<title>Sketch Onward Club</title>
<link href="https://fonts.googleapis.com/css2?family=Audiowide&family=Orbitron:wght@400&family=Open+Sans:wght@400;600&display=swap" rel="stylesheet">
<style>
:root{
  --pink:#ee3d8c;
  --pink-deep:#e0287a;
  --teal:#3dbdcf;
  --green:#8dc63f;
  --ink:#333333;
  --muted:#777777;
  --line:#dddddd;
  --soft:#f6f6f6;
  --white:#ffffff;
}
*{margin:0;padding:0;box-sizing:border-box}
html,body{width:748px;height:1200px;overflow:hidden;background:var(--white)}
body{position:relative;font-family:"Open Sans",Arial,sans-serif;color:var(--ink)}
.abs{position:absolute}

/* header */
.site-header{left:0;top:0;width:748px;height:34px;background:var(--white)}
.brand{left:56px;top:9px;font-size:9px;font-weight:600;color:var(--pink);display:flex;align-items:center;gap:4px}
.brand-dot{width:9px;height:9px;border-radius:50%;background:var(--teal)}
.main-nav{right:132px;top:12px;display:flex;gap:17px;font-size:8px;color:var(--ink)}
.sign-in{left:628px;top:7px;width:63px;height:21px;border-radius:11px;background:var(--pink);color:var(--white);font-size:7.5px;font-weight:600;display:flex;align-items:center;justify-content:center;box-shadow:inset 0 0 0 2px var(--pink),inset 0 0 0 3px rgba(255,255,255,.7)}

/* hero */
.hero{left:0;top:34px;width:748px;height:340px;background:linear-gradient(90deg,#f4a21f 0%,#f26a2b 12%,#21b3d8 25%,#9b3fc4 38%,#ea4a95 46%,#ef4c91 100%)}
.hero-art{left:0;top:0;width:748px;height:340px}
.hero-title{left:342px;top:130px;font-family:"Audiowide",sans-serif;color:var(--white);line-height:1}
.hero-title .welcome{font-size:22px;display:block}
.hero-title .name-a{font-size:37px;display:block;margin-top:2px}
.hero-title .name-b{font-size:37px;display:block;margin-left:60px;margin-top:2px}

/* about */
.section-title{font-family:"Orbitron",sans-serif;font-weight:400;color:var(--pink)}
.about-title{left:55px;top:404px;font-size:20px}
.about-text{left:55px;top:432px;width:410px;font-size:9.2px;line-height:15px;color:var(--ink)}
.read-more{left:55px;top:520px;width:84px;height:27px;border-radius:14px;background:var(--teal);color:var(--white);font-size:7.5px;display:flex;align-items:center;justify-content:center;box-shadow:inset 0 0 0 3px var(--teal),inset 0 0 0 4px rgba(255,255,255,.6)}
.about-photo-large{left:507px;top:391px;width:187px;height:187px;border-radius:50%;border:3px solid var(--teal);background:linear-gradient(135deg,#8a7a5e,#c98b4a 45%,#6f8f4d)}
.about-photo-small{left:472px;top:462px;width:124px;height:124px;border-radius:50%;border:4px solid var(--green);background:linear-gradient(160deg,#f2e8e0,#d8b49a 60%,#b9a0c8)}

/* artwork */
.art-title{left:55px;top:612px;font-size:17px}
.arrow-btn{top:614px;width:18px;height:18px;display:flex;align-items:center;justify-content:center}
.arrow-prev{left:650px;background:var(--pink)}
.arrow-next{left:673px;background:var(--teal)}
.art-tile{top:646px;width:154px;height:129px}
.art-one{left:56px;background:linear-gradient(135deg,#1f2a3a,#b7a48f 55%,#2b2f3e)}
.art-two{left:217px;background:linear-gradient(135deg,#3b4fb0,#c23d4b 40%,#e9c34a 70%,#2f7a9a)}
.art-three{left:378px;background:linear-gradient(180deg,#f07ab0,#ee5d9c)}
.art-four{left:538px;background:linear-gradient(135deg,#c9ccd2,#8a7866 50%,#e3e4e8)}
.art-overlay{position:absolute;inset:0;background:rgba(238,61,140,.72);display:flex;flex-direction:column;align-items:center;justify-content:center;color:var(--white)}
.art-overlay .label{font-size:8px;margin-top:-2px}
.art-overlay .view{margin-top:5px;padding:4px 12px;border:1px solid var(--white);border-radius:11px;font-size:7.5px}

/* contact */
.contact-band{left:0;top:816px;width:748px;height:272px;background:var(--soft)}
.write-title{left:56px;top:842px;font-size:15px}
.field{left:56px;width:301px;background:var(--white);border:1px solid var(--line);font-size:7px;color:#aaaaaa;padding:8px 9px}
.f-name{top:867px;height:26px}
.f-email{top:898px;height:26px}
.f-message{top:929px;height:88px}
.send-btn{left:56px;top:1022px;width:301px;height:26px;background:var(--pink);color:var(--white);font-size:9px;font-weight:600;display:flex;align-items:center;justify-content:center}
.meet-title{left:373px;top:842px;font-size:15px}
.meet-lead{left:374px;top:863px;font-size:7.5px;color:var(--ink)}
.meet-country{left:374px;top:879px;font-size:8px;color:#1e73be}
.meet-line{left:374px;font-size:7.5px;color:var(--ink);display:flex;align-items:center;gap:7px}
.meet-address{top:897px}
.meet-phone{top:912px}
.map{left:373px;top:932px;width:317px;height:123px;background:linear-gradient(135deg,#e4e4e4,#d2d2d2 50%,#e8e8e8);border:1px solid var(--line)}

/* partners */
.partner{top:1105px;width:122px;height:48px;border:1px solid var(--line);display:flex;align-items:center;justify-content:center;gap:5px;font-size:11px;font-weight:600;color:#444444}
.partner-mark{width:11px;height:11px;border-radius:50%;background:var(--teal)}
.p1{left:56px}.p2{left:185px}.p3{left:313px}.p4{left:442px}.p5{left:570px}

/* footer */
.site-footer{left:0;top:1168px;width:748px;height:32px;background:var(--pink);color:var(--white);font-size:7.5px;display:flex;align-items:center;justify-content:center}
</style>
</head>
<body>

<header class="site-header abs">
  <div class="brand abs"><span class="brand-dot"></span>Sketch Onward Club</div>
  <nav class="main-nav abs">
    <span>Find a Drawing</span><span>About</span><span>FAQ</span><span>Contact</span><span>Report</span><span>Our Policies</span>
  </nav>
  <div class="sign-in abs">SIGN IN</div>
</header>

<section class="hero abs">
  <div class="hero-art abs" role="img" aria-label="Colourful low-poly shapes over a pink-tinted street mural"></div>
  <h1 class="hero-title abs">
    <span class="welcome">Welcome To</span>
    <span class="name-a">Sketch Onward</span>
    <span class="name-b">Club</span>
  </h1>
</section>

<section class="about">
  <h2 class="section-title about-title abs">About Us</h2>
  <p class="about-text abs">“We believe that the gift of hand-made art –a simple drawing with a nice message for a stranger can brighten somone’s day and make the world just a little bit better. We also believe everyone is an artist, whether or not you’ve had any training or thinkyou have anyartistic talent. We created Sketch Onward Club to join people together through art, creating an artistic chain of smiling people linked together through the simple act of drawing.”</p>
  <div class="read-more abs">READ MORE</div>
  <div class="about-photo-large abs" role="img" aria-label="Large wall mural painted on a building"></div>
  <div class="about-photo-small abs" role="img" aria-label="Portrait photo of a thoughtful young woman"></div>
</section>

<section class="artwork">
  <h2 class="section-title art-title abs">RECENTLY ARTWORK</h2>
  <div class="arrow-btn arrow-prev abs"><svg width="6" height="8" viewBox="0 0 6 8"><path d="M5 1 L2 4 L5 7" stroke="#fff" stroke-width="1.3" fill="none"/></svg></div>
  <div class="arrow-btn arrow-next abs"><svg width="6" height="8" viewBox="0 0 6 8"><path d="M1 1 L4 4 L1 7" stroke="#fff" stroke-width="1.3" fill="none"/></svg></div>
  <div class="art-tile art-one abs" role="img" aria-label="Digital artwork of a woman surrounded by glowing light"></div>
  <div class="art-tile art-two abs" role="img" aria-label="Colourful graffiti wall"></div>
  <div class="art-tile art-three abs" role="img" aria-label="Street of old buildings under a pink overlay">
    <div class="art-overlay"><span class="label">ART WORK</span><span class="view">View Art Work</span></div>
  </div>
  <div class="art-tile art-four abs" role="img" aria-label="Watercolour painting of two kittens beside a paint palette"></div>
</section>

<section class="contact-band abs"></section>
<h2 class="section-title write-title abs">Write to us</h2>
<div class="field f-name abs">First Name *</div>
<div class="field f-email abs">Your Email *</div>
<div class="field f-message abs">Message</div>
<div class="send-btn abs">SEND</div>

<h2 class="section-title meet-title abs">let’s meet up</h2>
<p class="meet-lead abs">Let’s talk in person about the business</p>
<p class="meet-country abs">UNITED KINGDOM</p>
<p class="meet-line meet-address abs">
  <svg width="6" height="8" viewBox="0 0 6 8"><path d="M3 0 A3 3 0 0 1 6 3 C6 5 3 8 3 8 C3 8 0 5 0 3 A3 3 0 0 1 3 0Z" fill="#ee3d8c"/><circle cx="3" cy="3" r="1.1" fill="#fff"/></svg>
  Linden Court – Harbour Lane Westbury – 7781 203
</p>
<p class="meet-line meet-phone abs">
  <svg width="7" height="7" viewBox="0 0 7 7"><path d="M1 0 L2.5 0 L3 2 L2 2.8 C2.5 3.8 3.2 4.5 4.2 5 L5 4 L7 4.5 L7 6 C7 6.6 6.6 7 6 7 C3 7 0 4 0 1 C0 .4 .4 0 1 0Z" fill="#ee3d8c"/></svg>
  Phone: +44 (0) 20946 117305
</p>
<div class="map abs" role="img" aria-label="Street map with a location pin"></div>

<section class="partners">
  <div class="partner p1 abs"><span class="partner-mark"></span>NORVEL</div>
  <div class="partner p2 abs">ROUNDLY</div>
  <div class="partner p3 abs">TAVIRO</div>
  <div class="partner p4 abs">Quellix</div>
  <div class="partner p5 abs">BRANTE</div>
</section>

<footer class="site-footer abs">Copyright 2016 | All Right Reserved</footer>

</body>
</html>
```